Business Card Design for BrightlaneReach.com

--I need a business card design for my company BrightlaneReach.com

I have attached my logo...I want the brightlane reach logo on the front of the business card, and then I want The Brightlane Chief on the back of it with my information.

I would like to see a light colored background as well as a dark colored background

FRONT:
BRIGHTLANE REACH LOGO
247 E. Pelham Row
5th Floor
San Diego CA 92384
www.BrightlaneReach.com

Advanced Website & App Development
Websites, Apps, Online Voucher Systems

Leading Edge Marketing Services
SMS, VB, SMM, SEM,

BACK:
BRIGHTLANE CHIEF LOGO
Dorian Welker
The Brightlane Chief
Call Or Text: 555-204-3378
Dorian@BrightlaneChief.com
www.BrightlaneChief.com

Target Market(s)

small business owners

Industry/Entity Type

Business Consultant

Contact Information for Business Card

FRONT:
BRIGHTLANE REACH LOGO
247 E. Pelham Row
5th Floor
San Diego CA 92384
www.BrightlaneReach.com

SMS, VB, SMM, SEM,

BACK:
BRIGHTLANE CHIEF LOGO
Dorian Welker
The Brightlane Chief
Dorian@BrightlaneChief.com
www.BrightlaneChief.com

Requirements
Must have
• add this quote on it somewhere, anywhere,preferrably on back
• "The Fastest Way To Success Is To Take Action”
• — Dorian Welker, Brightlane Chief
Nice to have
• open
Should not have
• red

```html
<!DOCTYPE html>
<html lang="en">
<head>
<meta charset="utf-8">
<title>Brightlane Reach Business Card</title>
<link rel="stylesheet" href="https://fonts.googleapis.com/css2?family=Montserrat:wght@400;500;700;800&display=swap">
<style>
  :root {
    --bg-light: #e4e4e4;
    --bg-dark: #a9a9a9;
    --card: #0c0c0d;
    --card-edge: #18181a;
    --blue: #1b74ad;
    --blue-bright: #2a86c4;
    --white: #f2f2f2;
    --grey: #8a8a8a;
  }
  * { box-sizing: border-box; margin: 0; padding: 0; }
  html, body { width: 1200px; height: 1200px; overflow: hidden; }
  body {
    background: radial-gradient(ellipse at 40% 55%, var(--bg-light) 0%, #cfcfcf 50%, var(--bg-dark) 100%);
    font-family: "Montserrat", sans-serif;
    position: relative;
  }
  .card {
    position: absolute;
    left: 250px;
    width: 700px;
    height: 400px;
    background: radial-gradient(ellipse at 50% 40%, var(--card-edge) 0%, var(--card) 70%);
    box-shadow: 0 12px 30px rgba(0,0,0,0.35);
    overflow: hidden;
    color: var(--white);
  }
  .card--front { top: 150px; }
  .card--back { top: 650px; }

  .brand-name {
    position: absolute;
    font-weight: 500;
    color: var(--blue);
    letter-spacing: 8px;
    white-space: nowrap;
  }
  .card--front .brand-name { left: 0; right: 0; top: 100px; text-align: center; font-size: 46px; }
  .card--back .brand-name { right: 40px; top: 70px; font-size: 42px; }

  .icon { width: 22px; height: 22px; fill: var(--blue); flex: none; }

  /* front */
  .address {
    position: absolute; left: 40px; top: 250px;
    display: flex; gap: 14px; align-items: flex-end;
    font-size: 17px; line-height: 25px;
  }
  .address .icon { margin-bottom: 4px; }
  .divider { position: absolute; height: 1px; background: var(--blue); }
  .card--front .divider { left: 72px; top: 335px; width: 260px; }
  .website-row {
    position: absolute; left: 40px; top: 345px;
    display: flex; gap: 14px; align-items: center;
    font-size: 17px; color: var(--blue-bright);
  }
  .services {
    position: absolute; right: 30px; top: 265px; text-align: right;
    font-size: 12.5px; line-height: 18px; color: var(--blue-bright);
  }
  .service-tab {
    position: absolute; right: 0; bottom: 0; width: 310px; height: 70px;
    background: var(--blue); border-top-left-radius: 28px;
    padding: 10px 30px 0 0; text-align: right;
    font-size: 14px; font-weight: 700; line-height: 22px; color: var(--white);
  }

  /* back */
  .person-name {
    position: absolute; left: 55px; top: 170px;
    font-size: 26px; font-weight: 800; color: var(--blue); letter-spacing: 1px;
  }
  .card--back .divider { left: 55px; top: 212px; width: 330px; }
  .contact-list {
    position: absolute; left: 55px; top: 224px;
    list-style: none; font-size: 17px; line-height: 30px;
  }
  .contact-list li { display: flex; align-items: center; gap: 14px; }
  .contact-label { color: var(--blue-bright); }
  .quote-band {
    position: absolute; left: 150px; right: 0; bottom: 0; height: 70px;
    background: var(--blue); border-top-left-radius: 34px;
    display: flex; align-items: center; justify-content: center;
    font-size: 20px; font-weight: 500; color: var(--white);
  }
</style>
</head>
<body>
  <section class="card card--front" aria-label="Card front">
    <div class="brand-name">BRIGHTLANE REACH</div>

    <div class="address">
      <svg class="icon" viewBox="0 0 24 24" aria-hidden="true"><path d="M12 3 2 12h3v8h5v-5h4v5h5v-8h3z"/></svg>
      <div>247 E. Pelham Row<br>5th Floor<br>San Diego CA 92384</div>
    </div>
    <div class="divider"></div>
    <div class="website-row">
      <svg class="icon" viewBox="0 0 24 24" aria-hidden="true"><circle cx="12" cy="12" r="11"/><g fill="none" stroke="#0c0c0d" stroke-width="1.4"><circle cx="12" cy="12" r="6.5"/><ellipse cx="12" cy="12" rx="3" ry="6.5"/><path d="M5.5 12h13M6.5 9h11M6.5 15h11"/></g></svg>
      <span>www.BrightlaneReach.com</span>
    </div>

    <div class="services">
      Advanced Website &amp; App Development<br>
      Websites, Apps, Online Voucher Systems
    </div>
    <div class="service-tab">
      Leading Edge Marketing Services<br>
      SMS, VB, SMM, SEM
    </div>
  </section>

  <section class="card card--back" aria-label="Card back">
    <div class="brand-name">BRIGHTLANE CHIEF</div>

    <div class="person-name">DORIAN WELKER</div>
    <div class="divider"></div>
    <ul class="contact-list">
      <li>
        <svg class="icon" viewBox="0 0 24 24" aria-hidden="true"><path d="M6.6 10.8a15 15 0 0 0 6.6 6.6l2.2-2.2c.3-.3.7-.4 1-.2 1.1.4 2.3.6 3.6.6.6 0 1 .4 1 1V20c0 .6-.4 1-1 1A17 17 0 0 1 3 4c0-.6.4-1 1-1h3.5c.6 0 1 .4 1 1 0 1.3.2 2.5.6 3.6.1.3 0 .7-.2 1z"/></svg>
        <span><span class="contact-label">Call Or Text:</span> 555-204-3378</span>
      </li>
      <li>
        <svg class="icon" viewBox="0 0 24 24" aria-hidden="true"><path d="M2 5h20v14H2z"/><path d="M2 5l10 8 10-8M2 19l7-7M22 19l-7-7" fill="none" stroke="#0c0c0d" stroke-width="1.4"/></svg>
        <span>Dorian@BrightlaneChief.com</span>
      </li>
      <li>
        <svg class="icon" viewBox="0 0 24 24" aria-hidden="true"><circle cx="12" cy="12" r="11"/><g fill="none" stroke="#0c0c0d" stroke-width="1.4"><circle cx="12" cy="12" r="6.5"/><ellipse cx="12" cy="12" rx="3" ry="6.5"/><path d="M5.5 12h13M6.5 9h11M6.5 15h11"/></g></svg>
        <span>www.BrightlaneChief.com</span>
      </li>
    </ul>

    <div class="quote-band">“The Fastest Way To Success Is To Take Action”</div>
  </section>
</body>
</html>
```